New Office Poster Designs

Attached you will find 3 poster designs that we found online along with our logos. Please use our logos to reference any type of color or design.
These posters will be hung around our Loan Offices.

INSTRUCTIONS: Please mimic all 3 posters (MINUS THE SMALL WRITING ON THEM THAT IS NOT IN ENGLISH IGNORE THAT)
but use our logos and colors. Also, if you can make them in Spanish as well as English that is a plus. We will also need 1 additional poster with the below wording.

Additional Poster:
Stuck in a Title Loan? Let us pay it off up to $10,000

Target Market(s)

People looking to get a loan and need money

Industry/Entity Type

Loan Industry - Consumer Lending - Fast easy loans

Requirements
Nice to have
• English and Spanish

```html
<!DOCTYPE html>
<html lang="en">
<head>
<meta charset="UTF-8">
<title>No Credit Check Poster</title>
<link rel="stylesheet" href="https://fonts.googleapis.com/css2?family=Poppins:wght@500;700;800;900&display=swap">
<style>
  :root {
    --brand-green: #056d3b;
    --dot-red: rgba(201, 80, 80, 0.7);
    --dot-green: rgba(5, 109, 59, 0.5);
    --paper: #e4e4e2;
  }
  * { margin: 0; padding: 0; box-sizing: border-box; }
  html, body { width: 848px; height: 1200px; overflow: hidden; }
  body { font-family: "Poppins", sans-serif; background: var(--paper); }

  .poster {
    position: relative;
    width: 848px;
    height: 1200px;
    overflow: hidden;
  }
  .backdrop-photo {
    position: absolute; inset: 0;
    background:
      radial-gradient(ellipse 70% 30% at 45% 60%, rgba(232, 222, 198, 0.9), transparent 70%),
      linear-gradient(180deg, #d9d8d5 0%, #e6e5e2 35%, #dedbd2 60%, #d2d0cc 100%);
  }
  .accent-corner { position: absolute; }
  .accent-corner--top {
    top: 0; right: 0; width: 179px; height: 167px;
    background: radial-gradient(circle at 100% 0%, var(--dot-red) 0%, rgba(201,80,80,0.25) 55%, transparent 75%);
  }
  .accent-corner--bottom {
    bottom: 0; left: 0; width: 178px; height: 212px;
    background: radial-gradient(circle at 0% 100%, var(--dot-green) 0%, rgba(5,109,59,0.2) 55%, transparent 75%);
  }

  .brand {
    position: absolute;
    top: 104px; left: 0; width: 100%;
    display: flex; justify-content: center; align-items: center; gap: 10px;
  }
  .brand-mark { width: 14px; height: 14px; background: var(--brand-green); }
  .brand-name {
    font-weight: 700; font-size: 30px; color: var(--brand-green); line-height: 1;
  }

  .headline-no {
    position: absolute;
    top: 192px; left: -14px; width: 100%;
    text-align: center;
    font-weight: 900;
    font-size: 398px;
    line-height: 1;
    letter-spacing: -12px;
    color: var(--brand-green);
  }
  .headline-sub {
    position: absolute;
    top: 552px; left: -5px; width: 100%;
    text-align: center;
    font-weight: 800;
    font-size: 86px;
    line-height: 1;
    letter-spacing: -1px;
    color: var(--brand-green);
  }

  .feature-illustration {
    position: absolute;
    left: 240px; top: 734px;
    width: 434px; height: 214px;
    border-radius: 18px;
    background: linear-gradient(135deg, #8fd0a4 0%, #f3f5f8 35%, #3a7fd0 70%, #e24b4b 100%);
    opacity: 0.85;
  }

  .condition {
    position: absolute;
    top: 1045px; left: 0; width: 100%;
    text-align: center;
    font-weight: 800;
    font-size: 31px;
    line-height: 1;
    color: var(--brand-green);
  }
  .website {
    position: absolute;
    top: 1120px; left: 0; width: 100%;
    text-align: center;
    font-weight: 500;
    font-size: 32px;
    line-height: 1;
    color: var(--brand-green);
  }
  .tick-icon {
    position: absolute;
    left: 702px; top: 1110px;
    width: 80px; height: 62px;
  }
</style>
</head>
<body>
  <main class="poster">
    <div class="backdrop-photo" role="img" aria-label="Faded photo of a wooden tag reading no credit check on a desk with cash and a pen"></div>
    <div class="accent-corner accent-corner--top" role="img" aria-label="Red halftone dot accent"></div>
    <div class="accent-corner accent-corner--bottom" role="img" aria-label="Green halftone dot accent"></div>

    <header class="brand">
      <span class="brand-mark"></span>
      <span class="brand-name">Vantorly Loans</span>
    </header>

    <h1 class="headline-no">NO</h1>
    <h2 class="headline-sub">CREDIT CHECK</h2>

    <div class="feature-illustration" role="img" aria-label="Illustration of a credit report clipboard with a wallet, cash and a crossed-out credit card"></div>

    <p class="condition">WITH A CLEAR TITLE</p>
    <p class="website">www.vantorly.com</p>

    <svg class="tick-icon" viewBox="0 0 80 62" aria-hidden="true">
      <path d="M8 34 L28 54 L72 10" fill="none" stroke="#056d3b" stroke-width="9" stroke-linecap="round" stroke-linejoin="round"/>
    </svg>
  </main>
</body>
</html>
```